Blog Header Design + 2 Buttons + Colortheme

Hello,
I am looking for a fresh and catchy design for this blog project.
It can have a simplistic touch but I am open to all ideas which fit to the concept.
Please have a look at the pictures I've uploaded.
The website is called
http://www.wtwhn-blog.net
it is a blog which presents weird or extraordinary products. The URL is short for the german phrase "Was Toll Wäre Hier Nun?" it means "How cool is that?". Where "Geil" has the meaning of "Cool".
So yea, that is basically the idea of what it should stand for.
What I need is:
- a colortheme for the website
- a logo or banner at the top of the homesite (see the picture of the text I uploaded, if you could write it in this kind of deign that would look nice I guess)
- buttons for the product elements of the homesite and on the productdetail pages ("Geil!" Button and Price Button/Sign)
- background design (can fit the design idea but shouldnt be too distracting)
- if it is needed by or serves the design, the menu can be changed as well, but it can also stay as it is
optional for a complete set is needed:
- a favicon that fits the theme
- a facebook cover and profile picture
If you have any further questions please let know and I will respond to you as soon as possible.
Again, I am open to ALL design ideas for the whole website concept and would be glad to find a long term deign partner for other projects as well. THANK YOU!

```html
<!DOCTYPE html>
<html lang="en">
<head>
<meta charset="utf-8">
<title>Was Toll Wäre Hier Nun?</title>
<link href="https://fonts.googleapis.com/css2?family=Lato:wght@400;700;900&display=swap" rel="stylesheet">
<style>
:root{
  --page-bg:#ebebeb;
  --header-bg:#f3f3f3;
  --nav-top:#9a9a9a;
  --nav-bottom:#878787;
  --nav-active:#6e6e6e;
  --brand-green:#1f8f3c;
  --button-green:#14a14a;
  --button-green-dark:#0d7a35;
  --button-gray:#6d6d6d;
  --button-gray-dark:#4f4f4f;
  --price-orange:#f08400;
  --text:#444;
  --muted:#777;
  --line:#dcdcdc;
  --white:#fff;
}
*{box-sizing:border-box;margin:0;padding:0}
html,body{width:1152px;height:1200px;overflow:hidden}
body{font-family:'Lato',sans-serif;background:var(--page-bg);color:var(--text);position:relative}
.site-header{height:114px;background:var(--header-bg);position:relative}
.brand{position:absolute;left:154px;top:22px;color:var(--brand-green);font-weight:900;font-size:30px;line-height:32px;text-transform:uppercase;width:250px}
.lang{position:absolute;left:946px;top:19px;font-size:12px;color:var(--muted);display:flex;align-items:center;gap:6px}
.lang .flag{width:17px;height:11px;background:#8d9bb8;display:inline-block}
.lang .caret{width:0;height:0;border-left:3px solid transparent;border-right:3px solid transparent;border-top:4px solid #555}
.search{position:absolute;left:475px;top:67px;width:316px;height:31px;display:flex}
.search input{flex:1;border:1px solid #d6d6d6;border-right:none;background:#fff;font:13px 'Lato',sans-serif;padding:0 9px;color:#999}
.search .go{width:31px;border:1px solid #d6d6d6;background:#fff;display:flex;align-items:center;justify-content:center}
.social{position:absolute;left:804px;top:66px;display:flex;gap:9px}
.social span{width:32px;height:32px;border-radius:50%;display:block}
.social .s1{background:#4a6fc4}.social .s2{background:#c8312e}.social .s3{background:#3aa7e0}.social .s4{background:#2e3b4c}.social .s5{background:#f08c1a}
.main-nav{height:43px;background:linear-gradient(var(--nav-top),var(--nav-bottom));display:flex;padding-left:153px}
.main-nav a{color:#f3f3f3;text-decoration:none;font-size:13px;line-height:43px;padding:0 23px;white-space:nowrap}
.main-nav a.active{background:var(--nav-active);width:90px;padding:0;text-align:center}
.main-nav a:nth-child(2){padding-left:21px}
.promo{position:absolute;left:178px;top:175px;width:797px;height:173px;border:4px solid #c9c9c9;background:linear-gradient(135deg,#c4111c,#e02424 55%,#b50d17)}
.promo-close{position:absolute;left:957px;top:165px;width:27px;height:27px;border-radius:50%;background:#111;border:2px solid #fff;color:#fff;font-weight:900;font-size:14px;display:flex;align-items:center;justify-content:center}
.section-head{position:absolute;left:153px;top:369px;width:845px;height:34px;border-bottom:1px solid var(--line);display:flex;justify-content:space-between}
.section-head h1{color:var(--brand-green);font-size:18px;font-weight:700;line-height:34px}
.sort{display:flex;align-items:center;gap:9px;font-size:13px;color:#555}
.sort .select{width:118px;height:24px;background:#fff;border:1px solid #d6d6d6;font-size:12px;color:#999;padding-left:7px;line-height:22px;position:relative}
.sort .select::after{content:"";position:absolute;right:0;top:0;width:24px;height:22px;border-left:1px solid #d6d6d6}
.sort .select::before{content:"";position:absolute;right:7px;top:9px;border-left:4px solid transparent;border-right:4px solid transparent;border-top:5px solid #666}
.products{position:absolute;left:153px;top:419px;width:845px;display:grid;grid-template-columns:repeat(3,264px);column-gap:27px;row-gap:29px}
.card{background:var(--white);border:1px solid var(--line);height:303px;padding:7px 7px 0}
.card .media{height:185px;position:relative}
.card .caption{position:absolute;left:0;right:0;bottom:0;height:39px;background:rgba(40,40,40,.78);color:#fff;text-align:center;font-weight:700;font-size:18px;line-height:39px;text-transform:uppercase;white-space:nowrap}
.card .info{display:flex;justify-content:space-between;align-items:center;gap:6px;padding:6px 3px 0;height:52px}
.card .info p{font-size:12.5px;line-height:16px;flex:1 1 auto;min-width:0}
.card .price{color:var(--price-orange);font-weight:700;font-size:20px;white-space:nowrap;flex:0 0 auto}
.card .actions{display:flex;justify-content:space-between;padding:14px 4px 0}
.btn{height:33px;color:#fff;font-weight:700;font-size:13px;display:flex;align-items:center;justify-content:center;border-radius:2px;white-space:nowrap}
.btn-cool{width:93px;background:var(--button-green);border-bottom:3px solid var(--button-green-dark)}
.btn-details{width:118px;background:var(--button-gray);border-bottom:3px solid var(--button-gray-dark)}
.see-more{position:absolute;left:153px;top:1077px;width:845px;height:41px;background:#fafafa;border:1px solid var(--line);text-align:center;line-height:39px;font-size:12px;color:#555}
.site-footer{position:absolute;left:0;top:1150px;width:1152px;height:50px;background:var(--white);font-size:13px}
.site-footer .links{position:absolute;left:153px;top:18px;color:#555}
.site-footer .links span{margin:0 7px;color:#888}
.site-footer .copy{position:absolute;right:154px;top:19px;color:#999;font-size:12px}
.site-footer .copy b{color:var(--brand-green);font-weight:400}
</style>
</head>
<body>
<header class="site-header">
  <div class="brand">Was Toll Wäre Hier Nun?</div>
  <div class="lang">en <span class="flag"></span><span class="caret"></span></div>
  <form class="search"><input type="text" value="Search..."><span class="go"><svg width="14" height="14" viewBox="0 0 14 14"><circle cx="6" cy="6" r="4.5" fill="none" stroke="#666" stroke-width="1.6"/><line x1="9.3" y1="9.3" x2="13" y2="13" stroke="#666" stroke-width="1.8"/></svg></span></form>
  <div class="social"><span class="s1"></span><span class="s2"></span><span class="s3"></span><span class="s4"></span><span class="s5"></span></div>
</header>
<nav class="main-nav">
  <a class="active">Home</a><a>Technology</a><a>Fun &amp; Games</a><a>Clothing &amp; Accessories</a><a>Home &amp; Office</a><a>Food &amp; Drink</a><a>Others</a>
</nav>
<div class="promo" role="img" aria-label="Promotional banner with colourful hand lettering for a Christmas 0% financing offer"></div>
<div class="promo-close">x</div>
<div class="section-head">
  <h1>HOME</h1>
  <div class="sort">Sort by <div class="select">Price</div></div>
</div>
<main class="products">
  <article class="card"><div class="media" role="img" aria-label="Clothes hanging on a washing line outdoors" style="background:linear-gradient(#6f8f4a,#3f5a34)"><div class="caption">Bat Brackets</div></div><div class="info"><p>If the neighbor rings and tells you that hanging on...</p><span class="price">€ 6.62</span></div><div class="actions"><span class="btn btn-cool">COOL!</span><span class="btn btn-details">GET DETAILS</span></div></article>
  <article class="card"><div class="media" role="img" aria-label="Plaid mop slippers on feet" style="background:linear-gradient(#8a8e96,#b8b2aa)"><div class="caption">Shine Slippers</div></div><div class="info"><p>With this handy pair of cleaning and polishing shoes...</p><span class="price">€ 13.36</span></div><div class="actions"><span class="btn btn-cool">COOL!</span><span class="btn btn-details">GET DETAILS</span></div></article>
  <article class="card"><div class="media" role="img" aria-label="Cyclist wearing a clear umbrella dome" style="background:linear-gradient(#8fa37a,#3b4a34)"><div class="caption">Umbrella Dome</div></div><div class="info"><p>Hands free head dry, while funny look, here you are...</p><span class="price">€ 79.00</span></div><div class="actions"><span class="btn btn-cool">COOL!</span><span class="btn btn-details">GET DETAILS</span></div></article>
  <article class="card"><div class="media" role="img" aria-label="Child drinking through a colourful straw construction kit" style="background:linear-gradient(#d9dde0,#7ea15e)"><div class="caption">Straw Kit</div></div><div class="info"><p>The straw pipeline: Build your own tubes creations! ...</p><span class="price">€ 9.90</span></div><div class="actions"><span class="btn btn-cool">COOL!</span><span class="btn btn-details">GET DETAILS</span></div></article>
  <article class="card"><div class="media" role="img" aria-label="Girl hugging a large inflatable globe" style="background:linear-gradient(#6d7f8f,#3a4d6a)"><div class="caption">Giant Globe</div></div><div class="info"><p>Once around the world and in the living room. With this...</p><span class="price">€ 87.34</span></div><div class="actions"><span class="btn btn-cool">COOL!</span><span class="btn btn-details">GET DETAILS</span></div></article>
  <article class="card"><div class="media" role="img" aria-label="Woman pinning a photo to a magnetic painted wall" style="background:linear-gradient(#c97a95,#a9c46a)"><div class="caption">Magnetic Wall Paint</div></div><div class="info"><p>Simply turn wall surfaces quickly in a magnetic wall...</p><span class="price">€ 25.90</span></div><div class="actions"><span class="btn btn-cool">COOL!</span><span class="btn btn-details">GET DETAILS</span></div></article>
</main>
<div class="see-more">SEE MORE</div>
<footer class="site-footer">
  <div class="links">Site map<span>|</span>Term of use<span>|</span>Private policy</div>
  <div class="copy">© Copyrihgt 2013, <b>wtwhn</b>. All Rights Reserved</div>
</footer>
</body>
</html>
```